Loan broker seeks referral card design for real estate financing

We need a design for a referral card for people who recommend us for real estate financing. If the deal goes through, each referrer will receive €750.

Text similar to: Recommend me! For every successful real estate financing referral, you will receive €750. (Other suggestions are also welcome)

The size should be no larger than A5 format, or possibly even oblong.
The design should convey security and competence and include themes such as independent advice.

The design should also include the company logo and a photo of me. Naturally, the design should also include a link to my website: www.die-wandlinger.at, along with my phone number and email address: office@die-wandlinger.at

```html
<!DOCTYPE html>
<html lang="en">
<head>
<meta charset="utf-8">
<title>Referral Card – Wandlinger Vermögensberatung</title>
<link rel="stylesheet" href="https://fonts.googleapis.com/css2?family=Poppins:wght@400;500;600;700;800&display=swap">
<style>
  :root {
    --stage: #8c8c8c;
    --card: #ffffff;
    --brand: #1c4fb8;
    --brand-dark: #123c93;
    --ink: #2b2b2b;
    --rule: #9aa3b5;
    --photo-light: #eef1f6;
    --photo-mid: #b9c0cc;
    --photo-dark: #2c3445;
  }
  * { box-sizing: border-box; margin: 0; padding: 0; }
  html, body { width: 839px; height: 1200px; overflow: hidden; }
  body {
    background: var(--stage);
    font-family: "Poppins", sans-serif;
    color: var(--ink);
    position: relative;
  }
  .card {
    position: absolute;
    left: 58px;
    width: 722px;
    background: var(--card);
    overflow: hidden;
    box-shadow: 0 6px 18px rgba(0,0,0,.35);
  }
  .card--front { top: 22px; height: 558px; }
  .card--back { top: 615px; height: 515px; }

  /* brand lockup */
  .brand { display: flex; align-items: center; gap: 12px; }
  .brand__dot {
    width: 62px; height: 62px; border-radius: 50%;
    border: 4px solid var(--brand); flex: none;
  }
  .brand__name { font-weight: 600; font-size: 17px; color: var(--brand); line-height: 1.25; white-space: nowrap; }
  .brand__tag { font-weight: 400; font-size: 13px; color: var(--brand); white-space: nowrap; }

  .card--front .brand { position: absolute; left: 26px; top: 26px; z-index: 2; }

  /* photo area */
  .portrait {
    position: absolute; right: 0; top: 0; bottom: 0; width: 320px;
    background: radial-gradient(ellipse at 55% 30%, var(--photo-mid) 0%, var(--photo-light) 55%);
  }
  .portrait::after {
    content: ""; position: absolute; left: 20px; right: 0; bottom: 0; height: 280px;
    background: linear-gradient(180deg, #4a5468, var(--photo-dark));
    border-radius: 150px 150px 0 0;
  }

  .offer {
    position: absolute; left: 0; top: 118px; width: 430px; text-align: center;
  }
  .offer__title { font-weight: 800; font-size: 44px; color: var(--brand); line-height: 1.1; white-space: nowrap; }
  .offer__text { font-size: 16px; line-height: 1.35; margin-top: 6px; padding: 0 20px; }
  .offer__amount { font-weight: 800; font-size: 64px; color: var(--brand); line-height: 1.1; margin-top: 2px; }
  .offer__more { font-weight: 600; font-size: 18px; white-space: nowrap; }

  .contact-band { position: absolute; left: 0; bottom: 0; width: 722px; height: 200px; }
  .contact {
    position: absolute; left: 28px; bottom: 28px; color: #fff;
  }
  .contact__phone { font-weight: 700; font-size: 36px; letter-spacing: .5px; line-height: 1.2; }
  .contact__links { font-size: 14px; margin-top: 4px; }

  /* back */
  .card--back .brand { position: absolute; left: 50%; top: 70px; transform: translateX(-50%); }
  .referred {
    position: absolute; left: 50%; top: 200px; transform: translateX(-50%);
    background: var(--brand); color: #fff; font-weight: 700; font-size: 26px;
    padding: 6px 34px; border-radius: 14px; white-space: nowrap;
  }
  .field {
    position: absolute; left: 110px; right: 110px;
    display: flex; align-items: flex-end; gap: 14px;
    font-weight: 600; font-size: 19px;
  }
  .field__line { flex: 1; border-bottom: 2px dashed var(--rule); height: 1px; margin-bottom: 6px; }
  .field--name { top: 300px; }
  .field--email { top: 375px; }
</style>
</head>
<body>
  <section class="card card--front">
    <div class="portrait" role="img" aria-label="Portrait photo of the advisor in a dark suit"></div>

    <div class="brand">
      <span class="brand__dot"></span>
      <div>
        <div class="brand__name">Wandlinger Vermögensberatung GmbH</div>
        <div class="brand__tag">Finanzieren, Versichern, Vorsorgen</div>
      </div>
    </div>

    <div class="offer">
      <h1 class="offer__title">Recommend me!</h1>
      <p class="offer__text">For every successful real estate financing referral you will receive</p>
      <p class="offer__amount">€750</p>
      <p class="offer__more">Other Suggestions Are Also Welcome</p>
    </div>

    <svg class="contact-band" viewBox="0 0 722 200" preserveAspectRatio="none" aria-hidden="true">
      <path d="M0 40 Q230 -8 500 32 L500 200 L0 200 Z" fill="var(--brand-dark)"/>
      <path d="M0 54 Q230 8 500 46 L500 200 L0 200 Z" fill="var(--brand)"/>
    </svg>
    <div class="contact">
      <div class="contact__phone">+43 660 214 5830</div>
      <div class="contact__links">office@die-wandlinger.at &nbsp;|&nbsp; www.die-wandlinger.at</div>
    </div>
  </section>

  <section class="card card--back">
    <div class="brand">
      <span class="brand__dot"></span>
      <div>
        <div class="brand__name">Wandlinger Vermögensberatung GmbH</div>
        <div class="brand__tag">Finanzieren, Versichern, Vorsorgen</div>
      </div>
    </div>

    <div class="referred">Referred By</div>

    <div class="field field--name"><span>Name :</span><span class="field__line"></span></div>
    <div class="field field--email"><span>Email :</span><span class="field__line"></span></div>
  </section>
</body>
</html>
```